NEW STORE PROMOTION FLYER

We need a flyer design for a new lingerie store based in Double Bay.
The people living in Double Bay are most wealthy suburb in Sydney. Our customers are aged at 30+ to 70.
We are offering 'up to 30% off' on selected products.
we recommend using our theme colour: light pink, red, white
the address is:
shop 5/214 Larkmoor Vale Rd, NSW 2049
contact number: 02 8154 3907
We need key information:
1. we want to let neighborhood know that we open a new store.
2. we offer 'up to 30% off' Christmas Sale
3. Please use our theme colour: light pink, red, white
4. Please add the address map on flyer (you may design again if you need )
5.open hour:
Mon - Fri 10:00am - 5:30pm
Sat - Sun 10:00am - 5:30pm
thank you
aged 30+ to 70; they are relatively wealthy.
Store

```html
<!DOCTYPE html>
<html lang="en">
<head>
<meta charset="utf-8">
<title>Velouria Lingerie – New Store</title>
<link rel="stylesheet" href="https://fonts.googleapis.com/css2?family=Poppins:wght@400;500;700;800&family=Rokkitt:wght@500&display=swap">
<style>
  :root {
    --magenta: #e0137f;
    --magenta-soft: #e8489c;
    --blush-top: #f9dce6;
    --blush-mid: #fdeef3;
    --band: #f5a9b3;
    --label-box: #ebc2cc;
    --grey-serif: #d6b3bd;
    --ink: #2e2326;
    --white: #ffffff;
    --coral: #f39aa3;
  }
  * { margin: 0; padding: 0; box-sizing: border-box; }
  html, body { width: 849px; height: 1200px; overflow: hidden; background: var(--white); }
  .flyer {
    position: relative;
    width: 849px;
    height: 1200px;
    overflow: hidden;
    font-family: "Poppins", "Century Gothic", sans-serif;
    background: linear-gradient(180deg, var(--blush-top) 0%, var(--blush-mid) 55%, #fff8fa 72%);
  }
  .decor { position: absolute; }
  .decor-swirl-left {
    left: 0; top: 0; width: 200px; height: 370px;
    background: radial-gradient(ellipse at 30% 35%, rgba(224,19,127,.55), rgba(224,19,127,.12) 60%, transparent 75%);
  }
  .decor-stars-top {
    right: 0; top: 0; width: 320px; height: 220px;
    background: radial-gradient(ellipse at 60% 40%, rgba(255,255,255,.9), rgba(240,170,190,.35) 55%, transparent 75%);
  }
  .decor-swirl-right {
    right: 0; top: 400px; width: 300px; height: 470px;
    background: radial-gradient(ellipse at 65% 60%, rgba(243,154,163,.75), rgba(243,154,163,.25) 55%, transparent 75%);
  }
  .decor-dancers {
    left: 300px; top: 560px; width: 300px; height: 310px;
    background: radial-gradient(ellipse at 50% 55%, rgba(238,190,210,.6), transparent 70%);
  }
  .decor-stars-left {
    left: 0; top: 620px; width: 280px; height: 280px;
    background: radial-gradient(ellipse at 40% 50%, rgba(255,255,255,.85), rgba(240,175,195,.3) 55%, transparent 75%);
  }
  .store-heading {
    position: absolute; left: 148px; top: 104px;
    font-family: "Rokkitt", serif; font-weight: 500; font-size: 48px;
    color: var(--grey-serif); line-height: 1;
  }
  .brand-box {
    position: absolute; left: 148px; top: 150px; width: 292px; height: 98px;
    background: var(--label-box);
    padding: 18px 0 0 14px;
  }
  .brand-name {
    color: var(--magenta); font-weight: 500; font-size: 30px; line-height: 1.1;
  }
  .brand-sub {
    color: var(--magenta); font-weight: 500; font-size: 15px; letter-spacing: 6px;
    padding-left: 28px; margin-top: 4px;
  }
  .offer-lead {
    position: absolute; left: 176px; top: 340px;
    font-size: 34px; color: var(--magenta-soft); font-weight: 400;
  }
  .offer-value {
    position: absolute; left: 165px; top: 358px;
    font-size: 265px; font-weight: 700; color: var(--magenta);
    letter-spacing: -10px; line-height: 1; white-space: nowrap;
    transform: scaleX(.8); transform-origin: left top;
  }
  .offer-off {
    position: absolute; left: 602px; top: 389px;
    font-size: 110px; font-weight: 800; color: var(--magenta); line-height: 1;
    white-space: nowrap;
    transform: scaleX(.6); transform-origin: left top;
  }
  .offer-scope {
    position: absolute; left: 176px; top: 626px;
    font-size: 37px; font-weight: 700; color: var(--magenta); white-space: nowrap;
  }
  .info-band {
    position: absolute; left: 0; top: 868px; width: 849px; height: 332px;
    background: var(--band);
  }
  .stock-tag {
    position: absolute; left: 612px; top: 843px; width: 222px; height: 46px;
    border-radius: 23px;
    background: linear-gradient(90deg, var(--magenta) 0%, #ee5fa8 100%);
    color: var(--white); font-size: 19px; text-align: center; line-height: 46px;
  }
  .hours-tag {
    position: absolute; left: 0; top: 918px; width: 258px; height: 38px;
    background: var(--magenta); border-radius: 0 19px 19px 0;
    color: var(--white); font-weight: 700; font-size: 22px;
    padding-left: 42px; line-height: 38px;
  }
  .hours-list { position: absolute; left: 42px; top: 962px; list-style: none; }
  .hours-list li { font-size: 20px; color: var(--ink); line-height: 37px; }
  .hours-list b { font-weight: 700; }
  .address {
    position: absolute; left: 42px; top: 1064px;
    font-size: 21px; font-weight: 700; color: var(--ink); white-space: nowrap;
  }
  .contact {
    position: absolute; left: 42px; top: 1110px;
    font-size: 22px; color: var(--ink);
  }
  .contact b { font-weight: 700; }
  .location-map {
    position: absolute; left: 540px; top: 935px; width: 272px; height: 215px;
    background: linear-gradient(160deg, #fbd5da 0%, #f7bcc4 60%, #fde4e8 100%);
    border-radius: 4px;
  }
</style>
</head>
<body>
<main class="flyer">
  <div class="decor decor-swirl-left" role="img" aria-label="Magenta flourish ornament"></div>
  <div class="decor decor-stars-top" role="img" aria-label="White and pink star ornaments"></div>
  <div class="decor decor-swirl-right" role="img" aria-label="Coral pink flourish ornament"></div>
  <div class="decor decor-dancers" role="img" aria-label="Faint silhouettes of dancing women"></div>
  <div class="decor decor-stars-left" role="img" aria-label="White and pink star ornaments"></div>

  <p class="store-heading">new store</p>
  <div class="brand-box">
    <p class="brand-name">Velouria</p>
    <p class="brand-sub">Lingerie</p>
  </div>

  <p class="offer-lead">up to</p>
  <p class="offer-value">30%</p>
  <p class="offer-off">OFF</p>
  <p class="offer-scope">on selected products</p>

  <div class="info-band"></div>
  <p class="stock-tag">while stock last!</p>

  <p class="hours-tag">Opening hour:</p>
  <ul class="hours-list">
    <li><b>Mon - Fri</b> 10:00am - 5:30pm</li>
    <li><b>Sat - Sun</b> 10:00am - 5:30pm</li>
  </ul>
  <p class="address">shop 5/214 Larkmoor Vale Rd, NSW 2049</p>
  <p class="contact">contact no: <b>02 8154 3907</b></p>

  <div class="location-map" role="img" aria-label="Street map showing the store location"></div>
</main>
</body>
</html>
```